Menu Board For a Bubble Tea Trailer

Berrisip is a bubble tea trailer that will be located in town and by the beach. Our aim is to bring refreshing beverages to our local community. My menu needs to reflect a bubbly and happy atmosphere of delicious fruit and some floral drinks, without looking unprofessional or childish.

My menu needs to be 1600mm long by 500mm high. It will be printed and attached to a sneeze guard for my beverage trailer which will be displayed on my serving window.

All drinks are priced as follows:
Regular: $6.50 Large: $7.50
Extra Topping: $0.60

Target Market(s)

Ages 15-39 including high school students, and young to middle aged workers that feel they need an energy or mood boost.

Industry/Entity Type

Bubble Tea (Non Alcoholic beverage)

Font styles to use
Sans Serif
Script

Colors
0094D4
00A9DD
6FCCEA
C7EBF8
E9F6FB
00AB8E
00BBA5
67D7C9
C6EFE9
E9F9F6
EE7325
F08F49
F5BC92
FAE3D3
FDF4ED
EB3D1F
EC4F4E
F09395
F8D3D4
FCEDEE

Requirements
Must have
• Pictures of bubble tea, Not crowded, easy to read, complimentary colours, prices, pictures must be in round bottom cups and without lid (attached)
Nice to have
• Bubbles or wave pattern
Should not have
• No black background, no fruits, no cartoon looking pictures

```html
<!DOCTYPE html>
<html lang="en">
<head>
<meta charset="utf-8">
<title>Bubble Tea Menu Board</title>
<link href="https://fonts.googleapis.com/css2?family=Berkshire+Swash&family=Rosarivo&family=PT+Sans:wght@400;700&display=swap" rel="stylesheet">
<style>
  :root {
    --paper: #ece5d6;
    --paper-light: #f3eee3;
    --teal: #15b5b0;
    --teal-brush: #1cc0bd;
    --coral: #f7a08a;
    --menu-red: #c4504c;
    --white: #ffffff;
    --art-brown: #8a6244;
    --art-dark: #3a2a22;
    --art-tea: #d9a987;
    --art-milk: #f4f1ec;
  }
  * { margin: 0; padding: 0; box-sizing: border-box; }
  html, body { width: 1200px; height: 375px; overflow: hidden; background: var(--paper); }
  .board {
    position: relative; width: 1200px; height: 375px; overflow: hidden;
    background: radial-gradient(ellipse at 50% 40%, var(--paper-light), var(--paper) 75%);
    font-family: "PT Sans", sans-serif; color: var(--menu-red);
  }
  .art { position: absolute; border-radius: 6px; }
  .center { position: absolute; transform: translateX(-50%); text-align: center; white-space: nowrap; }
  .heading {
    font-family: "Berkshire Swash", cursive; color: var(--teal);
    font-size: 44px; line-height: 1;
  }
  .heading-tag {
    position: absolute; background: var(--coral); border-radius: 4px;
    font-family: "Rosarivo", serif; font-size: 19px; color: var(--menu-red);
    display: flex; align-items: center; justify-content: center; padding-top: 8px;
  }
  .flavour-list { font-size: 16px; line-height: 21.2px; }
  .flavour-list .sep { margin: 0 6px; }
  .topping-group { font-weight: 700; font-size: 16px; }
  .price-tag { position: absolute; width: 142px; height: 94px; }
  .price-tag svg { position: absolute; inset: 0; }
  .price-label {
    position: absolute; left: 0; right: 0; text-align: center; color: var(--white);
    font-weight: 700; font-size: 16px; line-height: 15px;
  }
  .price-amount {
    position: absolute; left: 0; right: 0; text-align: center; color: var(--white);
    font-weight: 700; font-size: 36px; line-height: 1;
  }
</style>
</head>
<body>
<main class="board">

  <div class="art" role="img" aria-label="Watercolour bowl of tapioca pearls"
       style="left:0;top:0;width:112px;height:121px;background:linear-gradient(135deg,#c9b79c,#7a5a40);opacity:.8"></div>
  <div class="art" role="img" aria-label="Watercolour tea strainer with loose tea"
       style="left:0;top:280px;width:100px;height:95px;background:linear-gradient(135deg,#a87a5a,#6a3d2a);opacity:.75"></div>
  <div class="art" role="img" aria-label="Watercolour glass jug of tea"
       style="left:1109px;top:0;width:91px;height:140px;background:linear-gradient(160deg,#b8a38b,#5e4632);opacity:.75"></div>
  <div class="art" role="img" aria-label="Watercolour cup of milk"
       style="left:1076px;top:280px;width:124px;height:95px;background:linear-gradient(160deg,var(--art-milk),#d8d2c8)"></div>
  <div class="art" role="img" aria-label="Watercolour coffee scoop"
       style="left:880px;top:296px;width:94px;height:79px;background:linear-gradient(135deg,#4a3a2c,#b07a4a);opacity:.7"></div>
  <div class="art" role="img" aria-label="Brown sugar cube"
       style="left:279px;top:14px;width:43px;height:40px;background:var(--art-brown);opacity:.8"></div>
  <div class="art" role="img" aria-label="Brown sugar cube"
       style="left:348px;top:75px;width:32px;height:31px;background:var(--art-brown);opacity:.8"></div>
  <div class="art" role="img" aria-label="Tapioca pearl"
       style="left:655px;top:13px;width:28px;height:29px;background:var(--art-dark);opacity:.85"></div>
  <div class="art" role="img" aria-label="Tapioca pearls"
       style="left:818px;top:280px;width:32px;height:48px;background:var(--art-dark);opacity:.85"></div>

  <div class="art" role="img" aria-label="Watercolour milk tea with tapioca pearls in a round-bottom cup, mint leaves and a dish of brown sugar cubes"
       style="left:594px;top:28px;width:307px;height:326px;background:linear-gradient(180deg,#c98a6a 0%,var(--art-tea) 40%,#7a4e38 100%);opacity:.85"></div>

  <!-- Tea -->
  <div class="center heading" style="left:192px;top:42px">Tea</div>
  <div class="heading-tag" style="left:146px;top:84px;width:94px;height:33px">Milk</div>
  <div class="center flavour-list" style="left:192px;top:136px">
    Original<span class="sep">|</span>Royal<span class="sep">|</span>Tiger Pearl<br>
    Taro<span class="sep">|</span>Lychee<span class="sep">|</span>Thai<span class="sep">|</span>Lavender<br>
    Young coconut<span class="sep">|</span>Rose<span class="sep">|</span>Mango<br>
    Watermelon<span class="sep">|</span>Strawberry<br>
    Banana<span class="sep">|</span>Honeydew
  </div>

  <!-- Ice Tea -->
  <div class="center heading" style="left:484px;top:42px">Ice Tea</div>
  <div class="heading-tag" style="left:418px;top:82px;width:133px;height:36px">Green/Red</div>
  <div class="center flavour-list" style="left:484px;top:136px">
    Pomegranate<span class="sep">|</span>Passionfruit<br>
    Mango<span class="sep">|</span>Lychee<span class="sep">|</span>Strawberry<br>
    Watermelon<span class="sep">|</span>Dragonfruit<br>
    Peach<span class="sep">|</span>Green apple<br>
    Grape
  </div>

  <!-- Toppings -->
  <div class="center heading" style="left:984px;top:42px;font-size:47px">Toppings</div>
  <div class="center topping-group" style="left:984px;top:94px;font-size:18.5px">Tapioca Pearls</div>
  <div class="center topping-group" style="left:984px;top:131px">Fruit Jelly</div>
  <div class="center flavour-list" style="left:984px;top:152px">
    Rainbow<span class="sep">|</span>Lychee<br>
    Mango<span class="sep">|</span>Peach<span class="sep">|</span>Grape
  </div>
  <div class="center topping-group" style="left:984px;top:210px">Popping Pearls</div>
  <div class="center flavour-list" style="left:984px;top:234px">
    Mango<span class="sep">|</span>Peach<span class="sep">|</span>Lychee<br>
    Strawberry<span class="sep">|</span>Passionfruit<br>
    Watermelon
  </div>

  <!-- Prices -->
  <div class="price-tag" style="left:116px;top:252px">
    <svg viewBox="0 0 142 94" aria-hidden="true"><path d="M10 6 L130 0 L126 18 L142 22 L134 46 L140 70 L128 88 L18 94 L22 76 L0 70 L12 48 L2 26 Z" fill="var(--teal-brush)"/></svg>
    <div class="price-label" style="top:18px">Regular</div>
    <div class="price-amount" style="top:36px">$6.50</div>
  </div>
  <div class="price-tag" style="left:270px;top:252px">
    <svg viewBox="0 0 142 94" aria-hidden="true"><path d="M14 4 L136 0 L130 20 L142 30 L132 50 L142 74 L124 92 L20 94 L26 76 L2 66 L14 46 L0 22 Z" fill="var(--teal-brush)"/></svg>
    <div class="price-label" style="top:18px">Large</div>
    <div class="price-amount" style="top:36px">$7.50</div>
  </div>
  <div class="price-tag" style="left:424px;top:244px">
    <svg viewBox="0 0 142 94" aria-hidden="true"><path d="M12 6 L134 0 L128 16 L142 28 L132 52 L140 72 L126 90 L16 94 L22 78 L0 68 L12 46 L2 24 Z" fill="var(--teal-brush)"/></svg>
    <div class="price-label" style="top:16px">Extra<br>Topping</div>
    <div class="price-amount" style="top:49px">$0.60</div>
  </div>

</main>
</body>
</html>
```